Web Design Project

We need the homepage and 7 interior pages designed as described below - design only:

Main Page
We like this template: http://www.quillbarrow.com/demo/52917.html

We also want a login dropdown similar to http://www.perloxa.com

We want the main page to be luxurious and sleek. We are a limo company that is dedicated to good service and creating an experience, and our front page should strongly reflect that. We do not want a very busy front page.

The main page should do primary things:

1. Make Reservations: We really like velmorta.com for this aspect of the site. That being said, velmorta is NOT the type of company we are.
2. Inform the customer of our most popular packages and give a sense of our professionalism and luxurious service.
3. There should be an area for a customer login
4. Menu should include the following: Home, Who We Are, Our Fleet, Custom Packages,
Testimonials, Book Your Ride!

For a starting point, we like this template http://www.quillbarrow.com/demo/52917.html

Rather than "start up, integrate, develop" we could have 3 of the more popular packages (or categories of packages). The bottom part would be fine. We could have a chirpnet feed, welcome, and our core principles. The one big change would be the addition of a "booking" area right smack in the middle of the page, where a customer could enter in trip data and see if the date was available.

-

About Us - Secondary Page
We like this ABOUT page template: http://www.quillbarrow.com/demo/63284.html

This is a really important page that people overlook, yet it is the most viewed page of a website after the homepage. We have come up with a bit of text to go on the about us page:

Who We Are: Brisbury Limo was founded on the core principle that every limo ride starts with personalized service from the instant you book your ride and continues after you step out of the car. You and your party are more than just our customers. We consider knowing your name and providing you with your choice of snacks and periodicals in the car just a few of the integral elements of the limousine experience. We are striving to revolutionize the limousine industry by creating a personal, friendly, timely, and professional experience. Brisbury Limo combines current technology and a modern fleet with good old-fashioned service to deliver you a personalized, luxury experience. We cater to every event, from business travel to proms and wedding, and everything in between.

We do all of this while maintaining competitive pricing to our peers.

Have a taste of high society...

-

Custom Packages - Secondary Page

This page will contain descriptions of the packages that we offer: Wedding, Prom, Business, etc. - there should be a thumbnail of each package with a description next to it. When you click on a thumbnail it will bring you to a detailed page of that particular package.

-

Custom Packages Interior Page - Secondary Page

In depth look at that particular package - for example, weddings - shows that we offer complimentary champagne, Just married sign, etc.

-

Fleet Page - Secondary Page

This page can be fairly basic. It will include photos of the vehicles along with descriptions and number of passengers, etc.

-

Testimonials Page - Secondary Page

This page will have testimonials from customers. We don't want a big block of text, but rather small testimonials that will expand within the page when you click on a "+" symbol. We like the way it looks when the testimonials are enclosed within a speech bubble image - still professional and classy, not cheesy.

-

Book your ride! - Secondary Page

This page will have a form on it - the same as the form on the homepage, where people can enter in information to check the availability of vehicles. We also want basic contact information on this page as well in case people want to call directly or e-mail.

Requirements
Must have
• - Book your reservation form on homepage
- Sleek, elegant feel
- Chirpnet feed

```html
<!DOCTYPE html>
<html lang="en">
<head>
<meta charset="utf-8">
<title>Brisbury Limo — Home</title>
<link rel="stylesheet" href="https://fonts.googleapis.com/css2?family=Oswald:wght@300;400;500;700&family=Lato:wght@400;700&display=swap">
<style>
  :root {
    --blue-deep: #0b3f86;
    --blue-main: #1261b8;
    --blue-bright: #1f74cc;
    --blue-panel: #0e4a97;
    --blue-title: #1466c2;
    --dark-bar: #2a2725;
    --nav-band: #dcdfe4;
    --white: #ffffff;
    --btn-grey: #d6dbe1;
    --text-soft: #e6eefa;
    --ink: #333;
  }
  * { box-sizing: border-box; margin: 0; padding: 0; }
  html, body { width: 877px; height: 1200px; overflow: hidden; }
  body {
    position: relative;
    font-family: "Lato", Arial, sans-serif;
    background: radial-gradient(ellipse at 50% 40%, var(--blue-bright) 0%, var(--blue-main) 45%, var(--blue-deep) 100%);
    color: var(--white);
  }
  .abs { position: absolute; }

  /* header */
  .topbar {
    left: 0; top: 0; width: 877px; height: 78px;
    background: linear-gradient(to bottom, #143e7a 0, #143e7a 11px, var(--dark-bar) 12px, #1f1c1b 78px);
  }
  .brand {
    left: 153px; top: 37px;
    font-family: "Lato", sans-serif; font-weight: 400;
    font-size: 15px; letter-spacing: 3px; color: var(--white);
    display: flex; align-items: center; gap: 4px; white-space: nowrap;
  }
  .brand .dot { width: 6px; height: 6px; border-radius: 50%; background: var(--white); }
  .btn {
    font-family: "Oswald", sans-serif; font-weight: 500;
    font-size: 11px; text-transform: uppercase; text-align: center;
    line-height: 21px; height: 21px;
  }
  .btn-register { left: 561px; top: 35px; width: 59px; background: var(--blue-title); color: var(--white); border: 1px solid #0a3f7d; }
  .btn-login { left: 632px; top: 35px; width: 58px; background: var(--btn-grey); color: var(--blue-title); border: 1px solid #fff; }

  /* hero */
  .hero {
    left: 0; top: 78px; width: 877px; height: 299px;
    background: linear-gradient(100deg, #5a5448 0%, #8a8f96 25%, #b9bec4 45%, #2b2b2e 58%, #3a3c40 70%, #c7ccd2 85%, #9aa0a7 100%);
  }
  .hero-arrow { top: 234px; }

  /* login dropdown */
  .login-panel {
    left: 533px; top: 73px; width: 186px; height: 159px;
    background: var(--white); border: 2px solid var(--blue-title);
    color: var(--ink);
  }
  .login-panel::before {
    content: ""; position: absolute; top: -8px; left: 124px;
    border-left: 7px solid transparent; border-right: 7px solid transparent;
    border-bottom: 7px solid var(--blue-title);
  }
  .login-title {
    position: absolute; left: 15px; top: 14px;
    font-family: "Oswald", sans-serif; font-weight: 500; font-size: 14px;
    color: var(--blue-title); text-transform: uppercase; white-space: nowrap;
  }
  .login-field {
    position: absolute; left: 15px; width: 155px; height: 20px;
    border: 1px solid #bfc4ca; font-size: 8px; color: #777; padding: 5px 6px;
  }
  .login-submit {
    position: absolute; left: 17px; top: 104px; width: 58px;
    background: var(--btn-grey); color: var(--blue-title);
  }
  .login-meta { position: absolute; top: 140px; font-size: 8px; color: #555; display: flex; align-items: center; gap: 3px; white-space: nowrap; }

  /* navigation */
  .nav {
    left: 0; top: 377px; width: 877px; height: 47px;
    background: linear-gradient(to bottom, #eef0f3, var(--nav-band));
    border-bottom: 1px solid #b8bdc5;
    display: flex; justify-content: center; align-items: center; gap: 6px;
    font-family: "Oswald", sans-serif; font-weight: 300; font-size: 17px;
    color: var(--blue-deep); text-transform: uppercase;
  }
  .nav .current { font-weight: 500; border-bottom: 2px solid var(--blue-deep); line-height: 21px; }
  .nav .sep { font-size: 11px; color: #6a7a90; }

  /* booking */
  .booking {
    left: 123px; top: 439px; width: 629px; height: 138px;
    background: var(--blue-panel); border: 1px solid #0a3a77;
    box-shadow: inset 0 0 30px rgba(0,0,0,.2);
  }
  .booking .divider { position: absolute; left: 313px; top: 10px; width: 1px; height: 118px; background: #2a66b0; }
  .label {
    position: absolute; font-family: "Oswald", sans-serif; font-weight: 300;
    font-size: 21px; text-transform: uppercase; white-space: nowrap;
  }
  .label small { font-weight: 500; font-size: 13px; }
  .input {
    position: absolute; height: 20px; background: var(--white);
    color: #222; font-size: 8px; padding: 5px 7px;
  }
  .datebox {
    position: absolute; top: 94px; display: flex; gap: 2px; align-items: center;
    font-family: "Oswald", sans-serif; font-weight: 500; font-size: 21px;
  }
  .datebox span.box {
    background: var(--white); color: var(--blue-deep);
    padding: 0 2px; line-height: 24px; height: 25px; border: 2px solid var(--white);
    outline: 1px solid var(--blue-deep); outline-offset: -3px;
  }
  .btn-calc { position: absolute; left: 334px; top: 71px; width: 86px; background: var(--btn-grey); color: var(--blue-title); border: 1px solid #fff; }

  /* packages */
  .package {
    top: 592px; width: 188px; height: 221px;
    background: var(--blue-panel); box-shadow: inset 0 0 25px rgba(0,0,0,.15);
    text-align: center;
  }
  .package .photo { position: absolute; left: 13px; top: 13px; width: 162px; height: 77px; border: 3px solid var(--blue-title); }
  .package h3 {
    position: absolute; left: 0; width: 100%; top: 96px;
    font-family: "Oswald", sans-serif; font-weight: 300; font-size: 27px; text-transform: uppercase;
  }
  .package p { position: absolute; left: 10px; width: 168px; top: 134px; font-size: 9px; line-height: 11.8px; color: var(--text-soft); }
  .btn-more { background: var(--btn-grey); color: var(--blue-title); width: 60px; border: 1px solid #fff; }
  .package .btn-more { position: absolute; left: 64px; top: 188px; }

  /* lower sections */
  .section-title {
    top: 833px; font-family: "Oswald", sans-serif; font-weight: 300; font-size: 27px; text-transform: uppercase;
  }
  .item { display: flex; gap: 9px; font-size: 9px; line-height: 11.8px; color: var(--text-soft); width: 187px; }
  .item svg { flex: none; margin-top: 1px; }
  .rule { height: 0; border-top: 1px dotted #b9cbe6; }
  .about-photo { left: 346px; top: 883px; width: 182px; height: 107px; border: 3px solid var(--blue-panel); background: linear-gradient(120deg, #6f7a86, #c8ccd0 45%, #f3f3f3 60%, #4d5560); }
  .about-text { left: 345px; top: 1003px; width: 187px; font-size: 9px; line-height: 11.8px; color: var(--text-soft); }
  .feed-nav { top: 1087px; width: 19px; height: 19px; background: var(--btn-grey); border: 1px solid #fff; }

  /* footer */
  .footer-rule { left: 124px; top: 1124px; width: 628px; }
  .footer-brand { left: 124px; top: 1163px; }
  .footer-copy { left: 285px; top: 1177px; font-size: 9px; letter-spacing: 1px; white-space: nowrap; }
  .social { top: 1159px; width: 18px; height: 18px; border-radius: 50%; background: #d9e3f0; }
</style>
</head>
<body>

<header>
  <div class="abs topbar"></div>
  <div class="abs brand"><span>BRISBURYLIMO</span><span class="dot"></span></div>
  <div class="abs btn btn-register">Register</div>
  <div class="abs btn btn-login">Login</div>
</header>

<div class="abs hero" role="img" aria-label="Photo of a chauffeur in a grey suit resting his hand on the hood of a silver stretch limousine"></div>
<svg class="abs hero-arrow" style="left:126px" width="18" height="32" viewBox="0 0 18 32"><path d="M15 2 L3 16 L15 30" fill="none" stroke="#1a6fd0" stroke-width="4"/></svg>
<svg class="abs hero-arrow" style="left:732px" width="18" height="32" viewBox="0 0 18 32"><path d="M3 2 L15 16 L3 30" fill="none" stroke="#1a6fd0" stroke-width="4"/></svg>

<div class="abs login-panel">
  <div class="login-title">Login to Brisbury Limo</div>
  <div class="login-field" style="top:44px">Email Address</div>
  <div class="login-field" style="top:74px">Password</div>
  <div class="btn login-submit">Login</div>
  <div class="login-meta" style="left:11px">
    <svg width="8" height="8" viewBox="0 0 8 8"><rect x=".5" y=".5" width="7" height="7" fill="#fff" stroke="#1466c2"/><path d="M1.5 4 L3.3 6 L6.5 1.8" fill="none" stroke="#1466c2" stroke-width="1.2"/></svg>
    Keep me Logged in
  </div>
  <div class="login-meta" style="left:110px">Passowrd Help?</div>
</div>

<nav class="abs nav">
  <span class="current">Home</span><span class="sep">-</span>
  <span>Who We Are</span><span class="sep">-</span>
  <span>Our Fleet</span><span class="sep">-</span>
  <span>Custom Packages</span><span class="sep">-</span>
  <span>Testimonials</span><span class="sep">-</span>
  <span>Book Your Ride</span>
</nav>

<section class="abs booking">
  <div class="label" style="left:26px;top:9px">Pickup *</div>
  <div class="input" style="left:26px;top:38px;width:268px">Address, Airpirt or Landmark</div>
  <div class="label" style="left:26px;top:64px">Pickup Date *</div>
  <div class="datebox" style="left:26px"><span class="box">10</span>-<span class="box">09</span>-<span class="box">2012</span></div>
  <div class="label" style="left:179px;top:64px">Pickup Time *</div>
  <div class="datebox" style="left:179px"><span class="box">09</span>:<span class="box">45</span><span class="box">PM</span></div>
  <div class="divider"></div>
  <div class="label" style="left:334px;top:9px">Drop Off * <small>By the Hour * Multiple Rides</small></div>
  <div class="input" style="left:334px;top:38px;width:268px">Address, Airpirt or Landmark</div>
  <div class="btn btn-calc">Calculate Price</div>
</section>

<article class="abs package" style="left:124px">
  <div class="photo" role="img" aria-label="Photo of a wedding party standing beside a white limousine" style="background:linear-gradient(90deg,#6b7a4e,#8b3a3a 40%,#2b2b2b 60%,#d8d8d8)"></div>
  <h3>Wedding</h3>
  <p>Sui blanditiistes es praetiuptatum delenitimatququdolores etres quamolestiasexceuri sintsuincupaqui officia.</p>
  <div class="btn btn-more">More</div>
</article>
<article class="abs package" style="left:344px">
  <div class="photo" role="img" aria-label="Photo of a smiling prom guest holding yellow flowers in a limousine" style="background:linear-gradient(90deg,#3a3a3a,#e6d96a 35%,#d9b9a8 60%,#f4f4f4)"></div>
  <h3>Prom</h3>
  <p>Sui blanditiistes es praetiuptatum delenitimatququdolores etres quamolestiasexceuri sintsuincupaqui officia.</p>
  <div class="btn btn-more">More</div>
</article>
<article class="abs package" style="left:564px">
  <div class="photo" role="img" aria-label="Photo of a chauffeur in a cap at the wheel" style="background:linear-gradient(90deg,#1d1d1f,#a88f7c 40%,#cfd6dc 70%,#7f8a93)"></div>
  <h3>Business</h3>
  <p>Sui blanditiistes es praetiuptatum delenitimatququdolores etres quamolestiasexceuri sintsuincupaqui officia.</p>
  <div class="btn btn-more">More</div>
</article>

<section>
  <h2 class="abs section-title" style="left:124px">Testimonials</h2>
  <div class="abs item" style="left:128px;top:881px">
    <svg width="16" height="16" viewBox="0 0 16 16"><circle cx="8" cy="8" r="7" fill="none" stroke="#fff" stroke-width="1.5"/><path d="M4.5 8 L7 10.5 L11.5 5.5" fill="none" stroke="#fff" stroke-width="1.5"/></svg>
    <span>Sui blanditiistes es praetiuptatum delenitimatququdolores etres quamolestiasexceuri sintsuincupaqui officia.</span>
  </div>
  <div class="abs rule" style="left:124px;top:935px;width:187px"></div>
  <div class="abs item" style="left:128px;top:948px">
    <svg width="16" height="16" viewBox="0 0 16 16"><circle cx="8" cy="8" r="7" fill="none" stroke="#fff" stroke-width="1.5"/><path d="M4.5 8 L7 10.5 L11.5 5.5" fill="none" stroke="#fff" stroke-width="1.5"/></svg>
    <span>Sui blanditiistes es praetiuptatum delenitimatququdolores etres quamolestiasexceuri sintsuincupaqui officia.</span>
  </div>
  <div class="abs rule" style="left:124px;top:1004px;width:187px"></div>
  <div class="abs item" style="left:128px;top:1015px">
    <svg width="16" height="16" viewBox="0 0 16 16"><circle cx="8" cy="8" r="7" fill="none" stroke="#fff" stroke-width="1.5"/><path d="M4.5 8 L7 10.5 L11.5 5.5" fill="none" stroke="#fff" stroke-width="1.5"/></svg>
    <span>Sui blanditiistes es praetiuptatum delenitimatququdolores etres quamolestiasexceuri sintsuincupaqui officia.</span>
  </div>
  <div class="abs btn btn-more" style="left:125px;top:1086px">More</div>
</section>

<section>
  <h2 class="abs section-title" style="left:345px">Who We Are</h2>
  <div class="abs about-photo" role="img" aria-label="Photo of a woman in a white dress leaning on a white luxury car"></div>
  <p class="abs about-text">Sui blanditiistes es praetiupt massa laoreetues atum delenitimos atquq udolorese etres quamolestiasexceuri sintum piditaprdentimilique suincu paqui officia deserunt mollianimid estlaborum et dolorum massafugharum quidemed rerum facilis...</p>
  <div class="abs btn btn-more" style="left:346px;top:1086px">More</div>
</section>

<section>
  <h2 class="abs section-title" style="left:566px">Chirpnet</h2>
  <div class="abs item" style="left:567px;top:881px;width:186px">
    <svg width="20" height="20" viewBox="0 0 20 20"><circle cx="10" cy="10" r="7" fill="#fff"/></svg>
    <span>Lorem Ipsum is simply dummy text of the printing and typesetting industry. Lorem Ipsum has been the industry's standard dummy text ever since.</span>
  </div>
  <div class="abs rule" style="left:566px;top:935px;width:186px"></div>
  <div class="abs item" style="left:567px;top:948px;width:186px">
    <svg width="20" height="20" viewBox="0 0 20 20"><circle cx="10" cy="10" r="7" fill="#fff"/></svg>
    <span>Lorem Ipsum is simply dummy text of the printing and typesetting industry. Lorem Ipsum has been the industry's standard dummy text ever since.</span>
  </div>
  <div class="abs rule" style="left:566px;top:1004px;width:186px"></div>
  <div class="abs item" style="left:567px;top:1015px;width:186px">
    <svg width="20" height="20" viewBox="0 0 20 20"><circle cx="10" cy="10" r="7" fill="#fff"/></svg>
    <span>Lorem Ipsum is simply dummy text of the printing and typesetting industry. Lorem Ipsum has been the industry's standard dummy text ever since.</span>
  </div>
  <div class="abs feed-nav" style="left:567px">
    <svg width="17" height="17" viewBox="0 0 17 17"><path d="M13 8.5 H4 M8 4.5 L4 8.5 L8 12.5" fill="none" stroke="#1466c2" stroke-width="2"/></svg>
  </div>
  <div class="abs feed-nav" style="left:589px">
    <svg width="17" height="17" viewBox="0 0 17 17"><path d="M4 8.5 H13 M9 4.5 L13 8.5 L9 12.5" fill="none" stroke="#1466c2" stroke-width="2"/></svg>
  </div>
</section>

<footer>
  <div class="abs rule footer-rule"></div>
  <div class="abs brand footer-brand"><span>BRISBURYLIMO</span><span class="dot"></span></div>
  <div class="abs footer-copy">© 2012 | Privacy Policy</div>
  <div class="abs social" style="left:636px"></div>
  <div class="abs social" style="left:660px"></div>
  <div class="abs social" style="left:684px"></div>
  <div class="abs social" style="left:708px"></div>
  <div class="abs social" style="left:732px"></div>
</footer>

</body>
</html>
```